Northern Plains Trades Motor Guild
Where Local Trades Thrive
Simple
Marco Brenn
President & CEO
214 - 27480 Corbett Rd
Box 46712 Ferncliff
Alder Ridge, BC
V2K 4N7
marcobrenn@nptmg.example
www.nptmg.example

```html
<!DOCTYPE html>
<html lang="en">
<head>
<meta charset="utf-8">
<title>Northern Plains Trades Motor Guild — Stationery</title>
<link href="https://fonts.googleapis.com/css2?family=Open+Sans:wght@400;700&display=swap" rel="stylesheet">
<style>
:root{
  --board:#e3cfa9;
  --paper:#ffffff;
  --brand:#1f5fae;
  --brand-deep:#153f7c;
  --brand-light:#5d97dd;
  --ghost:#e4ebf4;
  --slate:#55585d;
  --ink:#4a4a4a;
  --label:#6a5a40;
}
*{box-sizing:border-box;margin:0;padding:0}
html,body{width:1200px;height:446px;overflow:hidden}
body{background:var(--board);font-family:"Open Sans",Arial,sans-serif;position:relative;color:var(--ink)}
.sheet{position:absolute;background:var(--paper);box-shadow:0 1px 3px rgba(0,0,0,.25);overflow:hidden}
.sheet svg{display:block}
.label{position:absolute;font-size:6px;letter-spacing:.8px;text-transform:uppercase;color:var(--label);white-space:nowrap}
.mark{position:absolute;display:flex;align-items:center;gap:4px;font-weight:700;color:var(--brand);white-space:nowrap}
.mark .dot{border-radius:50%;background:var(--brand)}
.mark-md{font-size:13px}.mark-md .dot{width:10px;height:10px}
.mark-sm{font-size:9px}.mark-sm .dot{width:7px;height:7px}
.ghost-mark{position:absolute;left:0;right:0;text-align:center;color:var(--ghost);font-weight:700;white-space:nowrap}
.ghost-mark .tag{display:block;font-size:9px;line-height:12px;letter-spacing:1px}
.contact{position:absolute;font-size:3.6px;line-height:5px;color:var(--ink);white-space:nowrap}
.band{position:absolute;top:0;bottom:0;background:linear-gradient(90deg,var(--brand-deep),var(--brand-light))}
</style>
</head>
<body>

<!-- Business cards -->
<div class="label" style="left:19px;top:188px">Business Card Options</div>

<div class="sheet business-card-front" style="left:19px;top:158px;width:126px;height:54px">
  <div class="band" style="left:0;width:4px"></div>
  <div class="mark mark-sm" style="left:12px;top:8px"><span class="dot"></span>NPTMG</div>
  <div class="contact" style="left:12px;top:27px"><strong>Marco Brenn</strong><br>President &amp; CEO<br>marcobrenn@nptmg.example</div>
  <div class="contact" style="right:7px;top:27px;text-align:right">214 - 27480 Corbett Rd<br>Alder Ridge, BC V2K 4N7<br>www.nptmg.example</div>
</div>
<div class="label" style="left:19px;top:220px">Business Card Front</div>

<div class="sheet business-card-back" style="left:19px;top:240px;width:126px;height:58px">
  <div class="mark mark-sm" style="left:12px;top:9px"><span class="dot"></span>NPTMG</div>
</div>
<div class="label" style="left:19px;top:309px">Business Card Back</div>

<!-- Letterhead option 1 -->
<div class="sheet letterhead" style="left:166px;top:19px;width:297px;height:394px">
  <div class="band" style="left:5px;width:9px"></div>
  <div class="mark mark-md" style="left:116px;top:14px"><span class="dot"></span>NPTMG</div>
  <div class="contact" style="right:16px;top:16px;text-align:right">214 - 27480 Corbett Rd<br>Box 46712 Ferncliff<br>Alder Ridge, BC V2K 4N7<br>www.nptmg.example</div>
  <div class="ghost-mark" style="top:232px;font-size:62px;line-height:70px">NPTMG<span class="tag">Where Local Trades Thrive</span></div>
</div>
<div class="label" style="left:283px;top:421px">Letterhead Option 1</div>

<!-- Letterhead option 2 -->
<div class="sheet letterhead" style="left:475px;top:19px;width:299px;height:394px">
  <div class="mark mark-md" style="left:117px;top:14px"><span class="dot"></span>NPTMG</div>
  <div class="ghost-mark" style="top:150px;font-size:62px;line-height:70px">NPTMG<span class="tag">Where Local Trades Thrive</span></div>
  <div class="contact" style="left:0;right:0;top:370px;text-align:center">214 - 27480 Corbett Rd · Box 46712 Ferncliff · Alder Ridge, BC V2K 4N7<br>marcobrenn@nptmg.example · www.nptmg.example</div>
</div>
<div class="label" style="left:593px;top:421px">Letterhead Option 2</div>

<!-- Envelope backs -->
<div class="sheet envelope-back" style="left:816px;top:7px;width:360px;height:72px">
  <svg width="360" height="72" viewBox="0 0 360 72">
    <defs><linearGradient id="flapBlue" x1="0" y1="0" x2="1" y2="0">
      <stop offset="0" stop-color="#2a6fc4"/><stop offset=".6" stop-color="#6ea3e3"/><stop offset="1" stop-color="#1a4f95"/></linearGradient></defs>
    <path d="M0 0H360V22Q180 62 0 22Z" fill="url(#flapBlue)"/>
    <path d="M0 22Q180 62 360 22" fill="none" stroke="#dde3ea" stroke-width="1"/>
  </svg>
</div>
<div class="sheet envelope-back" style="left:816px;top:91px;width:360px;height:76px">
  <svg width="360" height="76" viewBox="0 0 360 76">
    <path d="M0 0H360V22Q180 62 0 22Z" fill="var(--slate)"/>
  </svg>
</div>
<div class="sheet envelope-back" style="left:816px;top:175px;width:360px;height:70px">
  <svg width="360" height="70" viewBox="0 0 360 70">
    <path d="M0 0Q180 36 360 0" fill="none" stroke="#dde3ea" stroke-width="1"/>
  </svg>
  <div class="mark mark-sm" style="left:154px;top:30px"><span class="dot"></span>NPTMG</div>
</div>

<!-- Envelope front -->
<div class="sheet envelope-front" style="left:799px;top:259px;width:346px;height:106px">
  <div class="band" style="left:0;width:5px"></div>
  <div class="mark mark-sm" style="left:14px;top:10px"><span class="dot"></span>NPTMG</div>
  <div class="contact" style="left:14px;top:25px">214 - 27480 Corbett Rd<br>Box 46712 Ferncliff<br>Alder Ridge, BC V2K 4N7</div>
</div>
<div class="label" style="left:900px;top:373px">Envelope Option</div>

</body>
</html>
```